Meadowlark Counseling Partners, LLC Needs Modern Business Card Design.

We provide behavioral health services from western Kansas to eastern Kansas. There is an abundance of competition for the services we provide with our main competitor being larger and having significantly more financial resources; however, the quality of services we provide is greater and we have started to catch the attention of the State of Kansas. We had a great logo designed by ArtFolio - this will be used to build upon our brand. The logo (attached) should be used in the card development. We want something unique, modern, but also a card design that clearly states our name, contact info, provides the name and unqiue location of each clinician, etc. Rounded edges, or a unique size, just something that makes our business card stand out from others. I have also uploaded each clinician's name and their unique location and phone number.

Our idea is to have one side be black with our logo. Then, on the other side have business cards for each individual. Plus, we want one card that is "generic" with no specific clinician's name listed so that we can give clients an appointment card when they leave. Some clinicians have two locations - we're open to design and background color, but we have started going with branding colors of black, the yellow in the logo files attached, and sometimes a gray. Our new office has been decorated using this theme.

Target Market(s)

individuals and families in need of behavioral health services; potential professional referral sources; existing referral sources

Industry/Entity Type

Business

Contact Information for Business Card

I attached a Word doc that provides clinician names, credentials and location information specific to each individual.

Font styles to use
Serif

Colors
000000
fbed22
dbdbdb
9d9d9d
c3c3c3

Requirements
Must have
• 1) use of the company logo that has been attached; 2) a template that provides us space to individualize business cards for all of our clinicians; 3) should stick to the colors we are branding with: black, yellow from the logo file, maybe a gray shade and we're open to a suggestion on a shade of white.
Nice to have
• Group discussion culminated in the thought that one side would be black with just our logo - no clinician names, etc. A unique design - rounded edges, unique size, some catchy lay-out would be nice.
Should not have
• Must not be too busy. Should look "clean." The project should stick to branding colors: black, yellow (from the logo file), maybe a gray and shade of white.

```html
<!DOCTYPE html>
<html lang="en">
<head>
<meta charset="utf-8">
<title>Meadowlark Counseling Partners — Business Card</title>
<link href="https://fonts.googleapis.com/css2?family=Source+Sans+3:wght@400;600;700&family=Overpass:wght@500&display=swap" rel="stylesheet">
<style>
  :root {
    --backdrop: #d1d2d4;
    --card-white: #ffffff;
    --card-dark: #3a3a3c;
    --brand-yellow: #f8c512;
    --tagline-yellow: #fdd800;
    --text-gray: #555557;
    --rule-gray: #c3c3c3;
    --petal-tint: #fff4d8;
  }
  * { margin: 0; padding: 0; box-sizing: border-box; }
  html, body {
    width: 1200px;
    height: 1200px;
    overflow: hidden;
    background: var(--backdrop);
  }
  .canvas {
    position: relative;
    width: 1200px;
    height: 1200px;
  }
  .card {
    position: absolute;
    width: 708px;
    height: 423px;
    border-radius: 32px;
    overflow: hidden;
  }
  .card--front {
    left: 268px;
    top: 108px;
    background: var(--card-white);
  }
  .card--back {
    left: 277px;
    top: 628px;
    background: var(--card-dark);
    display: flex;
    align-items: center;
    justify-content: center;
  }
  .brand-decoration {
    position: absolute;
    left: 0;
    top: 0;
    width: 258px;
    height: 100%;
    background: radial-gradient(ellipse at 0% 58%, var(--petal-tint) 0%, var(--petal-tint) 45%, rgba(255,244,216,0.5) 70%, rgba(255,255,255,0) 100%);
  }
  .wordmark {
    position: absolute;
    left: 264px;
    top: 128px;
    font-family: "Source Sans 3", sans-serif;
    font-weight: 600;
    color: var(--brand-yellow);
    line-height: 1;
    text-transform: uppercase;
  }
  .wordmark__name {
    display: block;
    font-size: 42px;
    letter-spacing: 3px;
  }
  .wordmark__sub {
    display: block;
    margin-top: 8px;
    font-size: 19px;
    letter-spacing: 2.6px;
  }
  .wordmark-rule {
    position: absolute;
    left: 264px;
    top: 203px;
    width: 374px;
    height: 1px;
    background: var(--rule-gray);
  }
  .contact {
    position: absolute;
    right: 78px;
    top: 244px;
    text-align: right;
    font-family: "Source Sans 3", sans-serif;
    font-size: 22px;
    line-height: 29.5px;
    color: var(--text-gray);
  }
  .contact__name {
    font-weight: 700;
  }
  .tagline {
    font-family: "Overpass", sans-serif;
    font-weight: 500;
    font-size: 41px;
    letter-spacing: 1.5px;
    color: var(--tagline-yellow);
    line-height: 1;
    margin-top: 8px;
  }
</style>
</head>
<body>
  <main class="canvas">
    <section class="card card--front">
      <div class="brand-decoration" role="img" aria-label="Faint brand emblem decoration in pale yellow"></div>
      <h1 class="wordmark">
        <span class="wordmark__name">Meadowlark</span>
        <span class="wordmark__sub">Counseling Partners, LLC</span>
      </h1>
      <div class="wordmark-rule"></div>
      <address class="contact">
        <div class="contact__name">DANIEL R. HOLLIS, LP</div>
        <div>President</div>
        <div>145 N. Cedar St.</div>
        <div>Salina Kansas 67401</div>
        <div>785.555.0182</div>
      </address>
    </section>
    <section class="card card--back">
      <p class="tagline">LET THE SUNSHINE IN</p>
    </section>
  </main>
</body>
</html>
```